Parades of Thunder stationary design

Parades of Thunder (www.paradesofthunder.example) is a company that operates events that display the worlds most exotic cars, motorcyles, aircraft, watercraft and luxury brands. we are cutting edge and are looking for a clean , modern stationary design. our sponsors of the events include names like Veltrano, Morvane, Castelvetro, Kendrix, Bravoni, Lune Varet, Halvorsen and many other big names. we currently operate in florida but are looking to get into new York and California. I added the logo and two car images.car images are optional and not mandatory for the design. Just thought we would add to see what happens.

Target Market(s)

high end , clean design think KENDRIX DESGN style sharp, clean, cutting edge must appeal to the high end luxury brand corporate companies and car, motorcycle, boat, aircraft and luxury brand collectors

Industry/Entity Type

Events

Font styles to use
Sans Serif

Requirements
Must have
• our contact information
• Ray Dunmore
• President
• 352-555-0187
• www.paradesofthunder.example
• PO Box 4862
• Marlow, FL 32190
• for business card my email is ray@paradesofthunder.example

```html
<!DOCTYPE html>
<html lang="en">
<head>
<meta charset="utf-8">
<title>Parades of Thunder — Stationery</title>
<link rel="stylesheet" href="https://fonts.googleapis.com/css2?family=Raleway:wght@300;400;600;700&display=swap">
<style>
  :root {
    --backdrop: #e6e6e7;
    --paper: #ffffff;
    --ink: #4a4a4a;
    --ink-soft: #8a8a8a;
    --brand-grey: #7a7a7a;
    --brand-red: #c4161c;
    --band-grey: #9d9d9d;
    --card-black: #0d0d0d;
    --shadow: 0 4px 10px rgba(0,0,0,.28);
  }
  * { margin: 0; padding: 0; box-sizing: border-box; }
  html, body { width: 801px; height: 1200px; overflow: hidden; }
  body {
    background: var(--backdrop);
    font-family: "Raleway", "Helvetica Neue", Arial, sans-serif;
    color: var(--ink);
    position: relative;
  }

  /* ---------- wordmark ---------- */
  .wordmark {
    display: flex; align-items: center; gap: 7px;
    font-weight: 600; letter-spacing: .02em; white-space: nowrap;
  }
  .wordmark__dot { width: 7px; height: 7px; background: var(--brand-red); flex: none; }

  /* ---------- business cards ---------- */
  .card {
    position: absolute; width: 340px; height: 194px;
    box-shadow: var(--shadow); overflow: hidden;
  }
  .card--front { left: 40px; top: 56px; background: var(--card-black); }
  .card--front .card__photo {
    position: absolute; right: 0; top: 0; width: 62%; height: 100%;
    background: radial-gradient(ellipse at 65% 55%, #3a0d10 0%, #1c0b0c 40%, var(--card-black) 75%);
  }
  .card--front .wordmark {
    position: absolute; left: 0; right: 0; top: 84px; justify-content: center;
    color: #ffffff; font-size: 23px;
  }

  .card--back { left: 421px; top: 56px; background: var(--paper); }
  .card--back .wordmark {
    position: absolute; left: 18px; top: 24px; color: var(--brand-grey); font-size: 17px;
  }
  .card__person { position: absolute; right: 20px; top: 96px; text-align: right; }
  .card__name { color: var(--brand-red); font-weight: 700; font-size: 10.5px; letter-spacing: .04em; }
  .card__role { color: var(--ink-soft); font-size: 8px; margin-top: 2px; }
  .card__contact { position: absolute; left: 18px; top: 124px; font-size: 8px; line-height: 1.45; color: var(--ink-soft); }
  .card__contact .gap { height: 8px; }
  .label { color: var(--brand-red); font-weight: 600; }
  .card__web { position: absolute; right: 20px; bottom: 18px; font-size: 8px; color: var(--ink-soft); }
  .card__web strong, .sheet__web strong { color: var(--brand-red); font-weight: 600; }
  .card__band { position: absolute; left: 0; right: 0; bottom: 0; height: 6px; background: var(--band-grey); }
  .card__band::after {
    content: ""; position: absolute; right: 20px; width: 110px; height: 100%; background: var(--brand-red);
  }

  /* ---------- letterhead ---------- */
  .sheet {
    position: absolute; left: 100px; top: 300px; width: 600px; height: 848px;
    background: var(--paper); box-shadow: var(--shadow);
    font-size: 7.5px; line-height: 1.5; color: var(--ink-soft);
  }
  .sheet .wordmark {
    position: absolute; left: 86px; top: 52px; color: var(--brand-grey); font-size: 26px;
  }
  .sheet__date { position: absolute; left: 86px; top: 232px; }
  .sheet__to { position: absolute; left: 86px; top: 266px; }
  .sheet__body { position: absolute; left: 86px; top: 385px; width: 430px; }
  .sheet__body p { margin-bottom: 9px; }
  .sheet__body .indent { text-indent: 10px; }
  .sheet__closing { position: absolute; left: 86px; top: 581px; }
  .sheet__address { position: absolute; left: 86px; top: 755px; }
  .sheet__contact { position: absolute; left: 86px; top: 787px; }
  .sheet__web { position: absolute; right: 88px; top: 798px; }
  .sheet__band { position: absolute; left: 0; right: 0; bottom: 0; height: 12px; background: var(--band-grey); }
  .sheet__band::after {
    content: ""; position: absolute; left: 402px; width: 108px; height: 100%; background: var(--brand-red);
  }
</style>
</head>
<body>

  <!-- business card, front -->
  <section class="card card--front">
    <div class="card__photo" role="img" aria-label="Dark photograph of an exotic sports car in deep red and black tones"></div>
    <div class="wordmark"><span class="wordmark__dot"></span>Parades of Thunder</div>
  </section>

  <!-- business card, back -->
  <section class="card card--back">
    <div class="wordmark"><span class="wordmark__dot"></span>Parades of Thunder</div>
    <div class="card__person">
      <div class="card__name">RAY DUNMORE</div>
      <div class="card__role">President</div>
    </div>
    <div class="card__contact">
      <div>PO Box 4862</div>
      <div>Marlow, FL 32190</div>
      <div class="gap"></div>
      <div><span class="label">t.</span> 352-555-0187</div>
      <div><span class="label">e.</span> ray@paradesofthunder.example</div>
    </div>
    <div class="card__web">www.<strong>paradesofthunder</strong>.example</div>
    <div class="card__band"></div>
  </section>

  <!-- letterhead -->
  <section class="sheet">
    <div class="wordmark"><span class="wordmark__dot"></span>Parades of Thunder</div>

    <div class="sheet__date">Date:&nbsp;&nbsp;19.09.2014</div>
    <div class="sheet__to">
      To:&nbsp;&nbsp;Alex Morrow<br>
      Some Street, Some City<br>
      Some Country
    </div>

    <div class="sheet__body">
      <p>Dear Alex Morrow,</p>
      <p class="indent">Thank you for joining our season of rolling exhibitions. This letter confirms your place among our featured collectors and partners for the coming spring showcase along the Florida coast.</p>
      <p>Display bays open at dawn on both days, and our team will guide each vehicle to its marked position. Please send final entry details and insurance notes two weeks before arrival.</p>
      <p>We look forward to welcoming you and sharing another memorable weekend of craft, speed and design.</p>
    </div>

    <div class="sheet__closing">Best Wishes,</div>

    <div class="sheet__address">PO Box 4862<br>Marlow, FL 32190</div>
    <div class="sheet__contact">
      <span class="label">t.</span> 352-555-0187<br>
      <span class="label">e.</span> ray@paradesofthunder.example
    </div>
    <div class="sheet__web">www.<strong>paradesofthunder</strong>.example</div>
    <div class="sheet__band"></div>
  </section>

</body>
</html>
```